Website Design for a different kind of Business Consulting organisation needed!

We need a website design that reflects who we are, the simplicity of our consulting business and with a focus on our priority - to help our clients deliver, or execute - the "e" in Vantor-a.

Our key high level requirements are:
1) Simple and intuitive look and feel
2) Integration with all key social media platforms, chirpnet, pagebook, workring, scrollo.

10 pages, tops.
- Main page - Welcome
- About Us/ Who are Vantor-a?
- 5 services pages - Project Management, Business Process Management, Change Management, Business Analysis and Finance Systems
- Contact Us

Something like:
http://www.lmvholdings.example/

Vantor-a is a registered trademark and all Logos and other branded material are attached for reference.

So, what’s our gig: A few snippets from previous work...

We are a different kind of business consulting group. We partner with our clients to help them deliver change. We don't just provide them with the theory. We also provide them with the leadership and capability to execute the change.

We aren’t a one stop shop, and we don’t offer cookie cutter solutions. We’re a boutique consulting firm covering Project Management, Business Process Management, Change Management and Business Analytics.

Vantor-a is a professional services organisation that partners with their clients to lead the execution of strategic process and system improvement initiatives. Vantor-a combines hands on delivery with coaching in best practice methodologies and approaches to build their clients capabilities to ensure their ongoing success in project implementations.

UPDATES:

Thanks to everyone who has submitted designs so far. The standard of designs coming through is quite high, with lots of professional designs that nail the design brief. Eliminating them is proving to be quite challenging.

A few updates to the job brief:
- Please make sure the design fits on one page. We would like all of our information to be on the first page that people see without them having to scroll down
- Please ensure you include the FIVE services we offer in the design
- Please use corporate images/snapvault photos in your designs which are relevant to our business
- Please add a section for a live chirpnet feed from our chirpnet account and a link to plaza+
- Please add a section for news/updates

Also, if you are able to build a site once a design is selected, please let us know.

Thanks,

Marcela.

Target Market(s)

Our target customers are large enterprises in Australia that are growing rapidly and have recently (last 24 months) undertaken or are currently undergoing software implementations and business process improvement programs. These businesses have a turnover of $100m or above and are working hard to differentiate themselves from their competitors but are not seeing the return on investment promised by software vendors and process improvement initiatives.

Industry/Entity Type

Leadership

Requirements
Must have
• Collaboration / Training / Workshop / Consulting images all of a professional nature.
Simple, non-cluttered look with plenty of white space.

```html
<!DOCTYPE html>
<html lang="en">
<head>
<meta charset="utf-8">
<title>Vantor-a Pty Ltd</title>
<link href="https://fonts.googleapis.com/css2?family=Arimo:wght@400;700&family=Oswald:wght@400&family=Cabin+Condensed:wght@400&display=swap" rel="stylesheet">
<style>
:root{
  --brand-blue:#1c4f99;
  --nav-blue:#1a4c8c;
  --hero-purple:#8452d9;
  --hero-purple-soft:#9a63d8;
  --frame-blue:#a9bde0;
  --frame-grey:#9aa3ad;
  --teal:#86d2dc;
  --magenta:#b2458e;
  --text:#333;
  --footer-bg:#e8e8e8;
  --footer-text:#444;
  --social-grey:#6e6e6e;
}
*{margin:0;padding:0;box-sizing:border-box}
html,body{width:1200px;height:1061px;overflow:hidden;background:#fff}
body{position:relative;font-family:"Arimo",Arial,sans-serif;color:var(--text)}
a{text-decoration:none;color:inherit}
.abs{position:absolute}

.brand{display:flex;flex-direction:column;align-items:flex-end;color:var(--brand-blue)}
.brand-name{line-height:1;letter-spacing:-.5px}
.brand-tag{line-height:1}
.brand-head{left:100px;top:26px}
.brand-head .brand-name{font-size:42px}
.brand-head .brand-tag{font-size:8px;margin-top:2px}
.brand-foot{left:882px;top:946px}
.brand-foot .brand-name{font-size:29px}
.brand-foot .brand-tag{font-size:6px;margin-top:1px}

.nav-link{top:47px;font-size:12.5px;font-weight:700;color:var(--nav-blue);text-transform:uppercase;letter-spacing:.2px;white-space:nowrap}
.social{display:flex;gap:3px}
.social a{font-size:8px;font-weight:700;color:#fff;padding:7px 3px;border-radius:2px;line-height:1}
.social-top{left:958px;top:45px}
.social-top a{background:var(--nav-blue)}
.social-foot{left:872px;top:911px}
.social-foot a{background:var(--social-grey)}

.hero{left:0;top:78px}
.hero-title{left:144px;top:253px;font-family:"Oswald",sans-serif;font-weight:400;font-size:34px;color:#fff;letter-spacing:.4px;line-height:1.2}
.hero-copy{left:141px;top:304px;width:415px;font-size:14px;line-height:22px;color:#fff;letter-spacing:.25px}
.hero-mark{left:140px;top:160px;font-size:88px;color:rgba(70,60,160,.35);letter-spacing:-2px;line-height:1}
.hero-photo{left:572px;top:110px;width:430px;height:330px}

.services-band{left:107px;top:475px;width:963px;height:238px;background:linear-gradient(90deg,#f2f2f4,#fff 20%,#fff 80%,#f2f2f4)}
.service{top:475px;width:300px;height:238px}
.service h3{position:absolute;top:53px;font-size:15px;font-weight:700;color:var(--brand-blue);letter-spacing:.3px}
.service p{position:absolute;top:81px;width:200px;font-size:14px;line-height:17px;color:var(--text)}
.learn-more{position:absolute;top:185px;font-size:10px;color:#5a3a6e;border:1px solid #bbb;border-radius:2px;padding:7px 11px;letter-spacing:.3px;background:#fff}

.news-head{left:123px;top:738px;font-size:14px;font-weight:700;color:#444}
.news-strip{left:149px;top:770px;width:883px;height:60px;background:linear-gradient(90deg,#f5f5f5,#fff 30%,#fff 70%,#f5f5f5)}
.news-arrow{top:773px;width:22px;height:28px;background:#fff}
.news-item{top:775px;display:flex;gap:10px;font-size:12px;line-height:18px;color:#333;width:280px}
.news-dot{flex:none;width:16px;height:16px;border-radius:50%;background:#5bb7ea;margin-top:2px}

.footer{left:0;top:860px;width:1200px;height:201px;background:var(--footer-bg);border-top:1px solid #cfcfcf}
.foot-col{top:893px;font-family:"Cabin Condensed",sans-serif;color:var(--footer-text);list-style:none}
.foot-col li{font-size:12.5px;line-height:22.5px}
.foot-col li.lead{font-size:13.5px}
</style>
</head>
<body>

<header>
  <a class="abs brand brand-head" href="#"><span class="brand-name">Vantor-a</span><span class="brand-tag">Pty Ltd</span></a>
  <nav>
    <a class="abs nav-link" href="#" style="left:392px">Home</a>
    <a class="abs nav-link" href="#" style="left:478px">About us</a>
    <a class="abs nav-link" href="#" style="left:588px">Who are Vantor-a?</a>
    <a class="abs nav-link" href="#" style="left:764px">Services</a>
    <a class="abs nav-link" href="#" style="left:873px">Contact</a>
  </nav>
  <div class="abs social social-top"><a href="#">pagebook</a><a href="#">workring</a><a href="#">chirpnet</a></div>
</header>

<section>
  <svg class="abs hero" width="1200" height="400" viewBox="0 78 1200 400" aria-hidden="true">
    <path d="M96 160 Q96 150 108 148 L1080 92 Q1100 92 1102 110 L1108 380 Q1108 396 1092 398 L122 462 Q108 462 108 448 Z" fill="var(--frame-grey)" opacity=".8"/>
    <path d="M104 112 Q104 100 118 100 L1060 82 Q1072 82 1072 96 L1096 430 Q1096 446 1080 446 L130 456 Q112 456 110 440 L96 410 Z" fill="var(--frame-blue)" opacity=".9"/>
    <path d="M116 128 Q116 112 132 110 L1060 104 Q1076 104 1076 120 L1078 402 Q1078 416 1062 418 L136 442 Q118 442 118 426 Z" fill="var(--hero-purple-soft)" opacity=".85"/>
    <path d="M118 140 Q118 124 134 122 L1060 114 Q1076 114 1076 130 L1078 396 Q1078 410 1062 412 L136 440 Q120 440 120 424 Z" fill="var(--hero-purple)"/>
  </svg>
  <span class="abs hero-mark" aria-hidden="true">Vantor-a</span>
  <div class="abs hero-photo" role="img" aria-label="Photo of three smiling business professionals, one giving a thumbs up" style="background:linear-gradient(180deg,rgba(235,238,245,.35),rgba(200,205,220,.55));border-radius:4px"></div>
  <h1 class="abs hero-title">WHO ARE VANTOR-A?</h1>
  <p class="abs hero-copy">Sed ut perspiciatis unde omnis iste natus error sit voluptatem accusantium doloremque laudantium, totam rem aperiam, eaque ipsa quae ab illo inventore</p>
</section>

<section>
  <div class="abs services-band"></div>

  <article class="abs service" style="left:107px">
    <svg width="300" height="238" class="abs" style="left:0;top:0" aria-hidden="true">
      <path d="M14 40 L24 32 L30 180 L20 186 Z" fill="var(--teal)"/>
      <path d="M22 30 Q22 24 30 24 L230 18 L236 36 L28 40 Z" fill="var(--magenta)"/>
      <path d="M180 20 L230 16 Q236 16 236 24 L236 36 L190 36 Z" fill="var(--teal)"/>
      <rect x="30" y="36" width="210" height="190" fill="#fff"/>
    </svg>
    <h3 style="left:39px">Project Management</h3>
    <p style="left:39px">Sed ut perspiciatis unde omnis iste natus error sit voluptatem accusantium doloremque lau-dantium, totam</p>
    <a class="learn-more" href="#" style="left:33px">LEARN MORE</a>
  </article>

  <article class="abs service" style="left:408px">
    <svg width="300" height="238" class="abs" style="left:0;top:0" aria-hidden="true">
      <path d="M20 44 L26 40 L28 180 L22 186 Z" fill="var(--teal)"/>
      <path d="M90 30 Q92 24 100 24 L270 34 Q282 36 282 48 L280 196 L272 40 Z" fill="var(--magenta)"/>
      <path d="M140 30 L262 32 L264 40 L140 40 Z" fill="var(--teal)"/>
      <rect x="26" y="38" width="246" height="188" fill="#fff"/>
    </svg>
    <h3 style="left:39px">Change Management</h3>
    <p style="left:39px">Sed ut perspiciatis unde omnis iste natus error sit voluptatem accusantium doloremque lau-dantium, totam</p>
    <a class="learn-more" href="#" style="left:42px">LEARN MORE</a>
  </article>

  <article class="abs service" style="left:770px">
    <svg width="300" height="238" class="abs" style="left:0;top:0" aria-hidden="true">
      <path d="M4 60 Q4 52 12 52 L20 50 L14 194 Z" fill="var(--magenta)"/>
      <path d="M30 30 L120 36 L220 20 Q228 20 228 30 L228 40 L30 40 Z" fill="var(--magenta)"/>
      <path d="M30 28 L100 30 L100 40 L30 40 Z" fill="var(--teal)"/>
      <path d="M278 60 L288 64 L284 150 L278 150 Z" fill="var(--teal)"/>
      <rect x="18" y="38" width="236" height="188" fill="#fff"/>
    </svg>
    <h3 style="left:40px">Business Analysis</h3>
    <p style="left:40px">Sed ut perspiciatis unde omnis iste natus error sit voluptatem accusantium doloremque lau-dantium, totam</p>
    <a class="learn-more" href="#" style="left:41px">LEARN MORE</a>
  </article>
</section>

<section>
  <h2 class="abs news-head">LATEST NEWS</h2>
  <div class="abs news-strip"></div>
  <svg class="abs news-arrow" style="left:120px" viewBox="0 0 22 28" aria-label="Previous"><path d="M13 8 L8 14 L13 20" stroke="#222" stroke-width="2.5" fill="none"/></svg>
  <svg class="abs news-arrow" style="left:1052px" viewBox="0 0 22 28" aria-label="Next"><path d="M9 8 L14 14 L9 20" stroke="#222" stroke-width="2.5" fill="none"/></svg>
  <div class="abs news-item" style="left:154px"><span class="news-dot"></span><span>Aliquam ac venenatis lacus. Morbi commodo a libero rhoncus vitae rhoncus odio blandit.</span></div>
  <div class="abs news-item" style="left:466px;top:776px"><span class="news-dot"></span><span>Lorem ipsum dolor sit amet, consectetur adipiscing elit. Aliquam ac venenatis lacus.</span></div>
  <div class="abs news-item" style="left:767px;top:777px"><span class="news-dot"></span><span>Venenatis a libero rhoncus vitae rhoncus odio blandit.</span></div>
</section>

<footer>
  <div class="abs footer"></div>
  <ul class="abs foot-col" style="left:140px"><li class="lead">Home</li><li class="lead">About</li><li class="lead">News</li><li class="lead">Contact</li></ul>
  <ul class="abs foot-col" style="left:260px"><li class="lead">Taxation</li><li>International</li><li>Corporate</li><li>Individual</li></ul>
  <ul class="abs foot-col" style="left:380px"><li class="lead">Accounting &amp; Advisory</li><li>Compliance &amp; Reporting</li><li>Audit</li><li>Valuations &amp; Corporate Review</li><li>Cashflow Management</li><li>Succession Planning</li><li>Forensic Accounting</li></ul>
  <ul class="abs foot-col" style="left:580px"><li class="lead">Pensions</li><li>International Pension Funds</li><li>Pension Transfers</li></ul>
  <div class="abs social social-foot"><a href="#">pagebook</a><a href="#">workring</a><a href="#">chirpnet</a></div>
  <a class="abs brand brand-foot" href="#"><span class="brand-name">Vantor-a</span><span class="brand-tag">Pty Ltd</span></a>
</footer>

</body>
</html>
```